Clinicians Prime Bold "NOT YOUR DADDY's CARD" clear Card make the card you always wanted

I need a stand out business card, I would like it to be crazy modern using a
clear plastic 30 mil card, let this be your PHD thesis in Card Design, make it fun and cutting edge. Make it Toxicology Lab meets Night Club. Colors are tans and browns with a hint of gold, because we test PEE (urine) and we call it Liquid Gold!!

Target Market(s)

it goes to Dr. Offices, but I want them to say wow Nice card, and I want our Salesmen to say" We are not your Fathers Lab" we are NEW BOLD and Different....

Industry/Entity Type

Plastic

Contact Information for Business Card

Clinician's Prime Toxicology 2873 Fernhollow Avenue SE | Atlanta, GA 30472
Phone: 404.555.0173 | Fax: 404.555.0174 my cell phone 404.555.0198 my email is Lionel@cliniciansprimetoxicology.example

CLIA#47K9315062 | Lionel Ashcombe, CEO, GED
www.cliniciansprimetoxicology.example

Requirements
Must have
• Clear Card design, I want it to be double sided, unless you can show me a design that can only need one side because it is that GOOD
Should not have
• Should not look like a conservative lab

```html
<!DOCTYPE html>
<html lang="en">
<head>
<meta charset="utf-8">
<title>Clinician's Prime Toxicology – Business Card</title>
<link rel="stylesheet" href="https://fonts.googleapis.com/css2?family=Arimo:wght@400&display=swap">
<style>
  :root {
    --backdrop: #d9d4cd;
    --card-top: #ece7e1;
    --card-bottom: #ddd6ce;
    --card-edge: rgba(255,255,255,0.55);
    --text-brown: #6b5b52;
    --brand-brown: #7a5e54;
    --tagline-rust: #8a4a1e;
    --accent-gold: #b8955f;
  }
  * { margin: 0; padding: 0; box-sizing: border-box; }
  html, body {
    width: 1200px; height: 970px; overflow: hidden;
    background: var(--backdrop);
  }
  .canvas { position: relative; width: 1200px; height: 970px; }
  .card {
    position: absolute; left: 100px; top: 186px;
    width: 1000px; height: 598px;
    border-radius: 28px;
    background: linear-gradient(160deg, var(--card-top) 0%, var(--card-bottom) 100%);
    border: 1px solid var(--card-edge);
    box-shadow: 0 6px 24px rgba(60,45,30,0.12);
    font-family: "Arimo", Arial, sans-serif;
    color: var(--text-brown);
  }
  .brand-mark {
    position: absolute; left: 220px; top: 120px;
    width: 80px; height: 80px; border-radius: 50%;
    background: var(--accent-gold);
  }
  .tagline {
    position: absolute; left: 340px; top: 76px;
    font-size: 20px; color: var(--tagline-rust); white-space: nowrap;
  }
  .brand-name {
    position: absolute; left: 340px; top: 116px;
    font-size: 46px; line-height: 54px; font-weight: 400;
    color: var(--brand-brown); white-space: nowrap;
  }
  .divider {
    position: absolute; left: 111px; top: 315px; width: 775px; height: 2px;
    background: linear-gradient(90deg, rgba(140,110,80,0.2), #8c6e50 30%, #8c6e50 70%, rgba(140,110,80,0.2));
  }
  .contacts { position: absolute; left: 118px; top: 332px; list-style: none; }
  .contacts li {
    position: relative; padding-left: 33px;
    height: 34px; line-height: 34px; font-size: 21px; white-space: nowrap;
  }
  .contacts svg { position: absolute; left: 0; top: 8px; width: 20px; height: 20px; fill: var(--text-brown); }
  .person { position: absolute; right: 117px; top: 330px; text-align: right; }
  .person-name { font-size: 32px; line-height: 38px; }
  .person-title { font-size: 21px; line-height: 26px; }
  .address {
    position: absolute; right: 117px; top: 468px; text-align: right;
    font-size: 21px; line-height: 34px; font-style: normal;
  }
</style>
</head>
<body>
<div class="canvas">
  <section class="card" aria-label="Clinician's Prime Toxicology business card">
    <div class="brand-mark" aria-hidden="true"></div>
    <p class="tagline">"Clarity Beyond The Numbers, Every Sample"</p>
    <h1 class="brand-name">Clinician's Prime<br>Toxicology</h1>

    <div class="divider"></div>

    <ul class="contacts">
      <li><svg viewBox="0 0 24 24" aria-hidden="true"><path d="M6.6 10.8a15.1 15.1 0 0 0 6.6 6.6l2.2-2.2a1 1 0 0 1 1-.25 11.4 11.4 0 0 0 3.6.57 1 1 0 0 1 1 1V20a1 1 0 0 1-1 1A17 17 0 0 1 3 4a1 1 0 0 1 1-1h3.5a1 1 0 0 1 1 1c0 1.25.2 2.45.57 3.57a1 1 0 0 1-.25 1z"/></svg>404&nbsp; 555&nbsp; 0173</li>
      <li><svg viewBox="0 0 24 24" aria-hidden="true"><path d="M7 3h10v4H7zM4 8h16a2 2 0 0 1 2 2v6h-4v5H6v-5H2v-6a2 2 0 0 1 2-2zm4 8v3h8v-3z"/></svg>404&nbsp; 555&nbsp; 0174</li>
      <li><svg viewBox="0 0 24 24" aria-hidden="true"><path d="M7 1h10a2 2 0 0 1 2 2v18a2 2 0 0 1-2 2H7a2 2 0 0 1-2-2V3a2 2 0 0 1 2-2zm0 3v11h10V4zm2 13v2h2v-2zm4 0v2h2v-2z"/></svg>404&nbsp; 555&nbsp; 0198</li>
      <li>CLIA#47K9315062</li>
      <li>Lionel@cliniciansprimetoxicology.example</li>
      <li>www.cliniciansprimetoxicology.example</li>
    </ul>

    <div class="person">
      <p class="person-name">Lionel Ashcombe</p>
      <p class="person-title">CEO, GED</p>
    </div>

    <address class="address">
      2873 Fernhollow Avenue SE<br>
      Atlanta, GA 30472
    </address>
  </section>
</div>
</body>
</html>
```